Business Card Design Project

Im an electrician and my company name is Brightway Electrical
My main work is installing Lighting and Power Points, Home Theater Systems, TVS, Phones and Data
Im looking a business card, something nice, clean, modern and not to cluttered
Im open to sugestions
I dont mind if the "Services" is on the back on the business card
colours black, grey, white or the blue colour of my logo are prefered but not compulsory
any questions just message me
and please make it so if i need to edit the writing can do it easy. maybe by making it a seperate layer ?
My Details are.
Name - Peter Hollis
Job Title - Licenced Electrician
Mobile - 027 530 2174
Email - peter@brightwayelectrical.co.nz
Web - www.brightwayelectrical.co.nz
Services
Residential / Commercial
Lighting & Power
Heating & Ventilation
Automation
Phone & Data
Home Cinema
Sound Systems
TV, Antenna & Satellite
Digital Upgrades

```html
<!DOCTYPE html>
<html lang="en">
<head>
<meta charset="utf-8">
<title>Brightway Electrical – Business Card Design</title>
<link href="https://fonts.googleapis.com/css2?family=Source+Sans+3:wght@400;600;700&display=swap" rel="stylesheet">
<style>
  :root {
    --stage: #000000;
    --label: #7d7f82;
    --card-white: #ffffff;
    --ink-grey: #5b6064;
    --brand-teal: #0aacbc;
    --on-teal: #ffffff;
  }
  * { margin: 0; padding: 0; box-sizing: border-box; }
  html, body { width: 1200px; height: 1200px; overflow: hidden; }
  body {
    position: relative;
    background: var(--stage);
    font-family: "Source Sans 3", "Myriad Pro", sans-serif;
  }
  .abs { position: absolute; white-space: nowrap; }

  .sheet-kicker { left: 337px; top: 64px; font-size: 23px; color: var(--label); }
  .sheet-title { left: 335px; top: 90px; font-size: 46px; color: var(--label); }
  .side-label { left: 337px; font-size: 23px; color: var(--label); }
  .side-label.front { top: 176px; }
  .side-label.back { top: 951px; }

  .card { position: absolute; left: 334px; width: 531px; height: 325px; }
  .card-front { top: 216px; background: var(--card-white); }
  .card-back { top: 617px; background: var(--brand-teal); }

  .contact { position: absolute; left: 188px; top: 28px; color: var(--ink-grey); }
  .contact-name { font-size: 21px; font-weight: 600; line-height: 1; }
  .contact-role { font-size: 15px; margin-top: 6px; }
  .contact-lines { margin-top: 19px; font-size: 17px; line-height: 22.5px; }

  .brand-mark { position: absolute; left: 30px; top: 202px; width: 58px; height: 58px; background: var(--brand-teal); }
  .brand-name { position: absolute; left: 104px; top: 196px; font-size: 37px; font-weight: 600; color: var(--brand-teal); line-height: 1.1; }
  .brand-tagline { position: absolute; left: 198px; top: 272px; font-size: 23px; color: var(--brand-teal); }

  .back-brand { position: absolute; left: 28px; top: 178px; font-size: 31px; font-weight: 600; color: var(--on-teal); line-height: 1.15; }
  .services { position: absolute; left: 253px; top: 32px; color: var(--on-teal); font-size: 21px; line-height: 27.2px; list-style: none; }
  .services-heading { font-weight: 700; }

  .specs { left: 337px; top: 1040px; color: var(--label); font-size: 19px; }
  .specs-heading { margin-bottom: 11px; }
  .specs-row { display: flex; line-height: 25px; }
  .specs-key { width: 85px; }
  .specs-colon { width: 16px; }
</style>
</head>
<body>
  <div class="abs sheet-kicker">Business Card Design</div>
  <div class="abs sheet-title">Creative 1</div>

  <div class="abs side-label front">Front</div>
  <section class="card card-front">
    <div class="contact">
      <div class="contact-name">Peter Hollis</div>
      <div class="contact-role">Licenced Electrician</div>
      <div class="contact-lines">
        <div>Mobile : 027 530 2174</div>
        <div>Email : peter@brightwayelectrical.co.nz</div>
        <div>www.brightwayelectrical.co.nz</div>
      </div>
    </div>
    <div class="brand-mark"></div>
    <div class="brand-name">Brightway Electrical</div>
    <div class="brand-tagline">Residential &amp; Commercial</div>
  </section>

  <section class="card card-back">
    <div class="back-brand">Brightway<br>Electrical</div>
    <ul class="services">
      <li class="services-heading">Services</li>
      <li>- Residential / Commercial</li>
      <li>- Lighting &amp; Power</li>
      <li>- Heating &amp; Ventilation</li>
      <li>- Automation</li>
      <li>- Phone &amp; Data</li>
      <li>- Home Cinema</li>
      <li>- Sound Systems</li>
      <li>- TV, Antenna &amp; Satellite</li>
      <li>- Digital Upgrades</li>
    </ul>
  </section>
  <div class="abs side-label back">Back</div>

  <div class="abs specs">
    <div class="specs-heading">Printing Specs</div>
    <div class="specs-row"><span class="specs-key">Trim size</span><span class="specs-colon">:</span><span>W: 90 cms x H: 5.5cms</span></div>
    <div class="specs-row"><span class="specs-key">Printing</span><span class="specs-colon">:</span><span>2 colour Spot ink</span></div>
    <div class="specs-row"><span class="specs-key">Stock</span><span class="specs-colon">:</span><span>200 gsm Regent Wove Diamond White</span></div>
  </div>
</body>
</html>
```